Allied Health business card / Logo update.

Update/revitalise our logo and business cards. The logo needs to be suitable not only for business cards but stationary, website and clothing as well.

We have had the same hand logo for 16 years and have a strong brand name with this. One idea, however, was to base the idea around the similarities between the spine and bamboo. I will attach some images.

We are uncertain with colour. Initially, we thought earthy greens and greys/charcoal. However, we would also consider blue/charcoal combination.

I have attached our existing logo and this is our website. http://www.harbourleafspinal.com.au

Target Market(s)

General public
This is the only card

Industry/Entity Type

Health Care

Contact Information for Business Card

Harbourleaf Chiropractic Centre
27 Willowmere Road (Cnr Banfield St and Willowmere Rd) Kellmore Bay
4/58 Thornbury St Ashvale
phone: 02 6571 4826
email: info@harbourleafspinal.com.au
web: harbourleafspinal.com.au

Marcus P. Helton
Cert. Rehab Therapist
Chiropractor
BSc(Hbr)., MChirop(Wlt)., MClinRehabNeuro(Brk)
MCRA, MANFA, VODA

Font styles to use
Serif
Sans Serif

Colors
acd037
85acd3
5c5c5c

Requirements
Must have
• Company name, Professional name with qualifications
• Contact details.

```html
<!DOCTYPE html>
<html lang="en">
<head>
<meta charset="utf-8">
<title>Harbourleaf Chiropractic Centre – Business Card</title>
<link rel="stylesheet" href="https://fonts.googleapis.com/css2?family=Oswald:wght@300;400&family=Roboto+Condensed:wght@400&display=swap">
<style>
  :root {
    --backdrop: #1d1d1d;
    --card: #f7f7f5;
    --ink: #1b1b1b;
    --accent: #f0b41c;
  }
  * { margin: 0; padding: 0; box-sizing: border-box; }
  html, body {
    width: 1200px; height: 800px; overflow: hidden;
    background: var(--backdrop);
  }
  .card {
    position: absolute; left: 100px; top: 95px;
    width: 1000px; height: 610px;
    background: var(--card);
    border-radius: 44px;
    font-family: "Roboto Condensed", "Arial Narrow", sans-serif;
    color: var(--ink);
  }
  .brand {
    position: absolute; left: 380px; top: 110px; width: 400px;
    text-align: center;
    font-family: "Oswald", "Arial Narrow", sans-serif;
    font-weight: 400; color: var(--ink);
    line-height: 1.05;
  }
  .brand-name { display: block; font-size: 62px; letter-spacing: 2px; text-transform: uppercase; }
  .brand-sub { display: block; font-size: 24px; letter-spacing: 3px; text-transform: uppercase; }
  .person {
    position: absolute; right: 510px; top: 250px; width: 420px;
    text-align: right;
  }
  .person-name {
    font-family: "Oswald", "Arial Narrow", sans-serif;
    font-weight: 300; font-size: 54px; line-height: 1.05;
    color: var(--accent); text-transform: uppercase;
  }
  .person-role { font-size: 30px; line-height: 1.15; margin-top: 2px; }
  .person-quals { font-size: 24px; line-height: 1.2; margin-top: 24px; }
  .divider {
    position: absolute; left: 510px; top: 270px;
    width: 2px; height: 270px; background: var(--accent);
  }
  .practice { position: absolute; left: 535px; top: 270px; width: 440px; }
  .practice-name { font-size: 29px; color: var(--accent); line-height: 1.2; }
  .practice-address { font-size: 29px; line-height: 1.2; margin-bottom: 14px; }
  .contact-list { list-style: none; }
  .contact-item {
    display: flex; align-items: center; gap: 12px;
    font-size: 29px; line-height: 1.45;
  }
  .contact-icon { width: 30px; height: 30px; flex: none; }
</style>
</head>
<body>
  <div class="card">
    <div class="brand">
      <span class="brand-name">Harbourleaf</span>
      <span class="brand-sub">Chiropractic Centre</span>
    </div>

    <div class="person">
      <div class="person-name">Marcus P. Helton</div>
      <div class="person-role">Cert. Rehab Therapist<br>Chiropractor</div>
      <div class="person-quals">BSc(Hbr)., MChirop(Wlt).<br>MClinRehabNeuro(Brk)<br>MCRA, MANFA, VODA</div>
    </div>

    <div class="divider"></div>

    <div class="practice">
      <div class="practice-name">Harbourleaf Chiropractic Centre</div>
      <div class="practice-address">27 Willowmere Road, Kellmore Bay<br>4/58 Thornbury St, Ashvale</div>
      <ul class="contact-list">
        <li class="contact-item">
          <svg class="contact-icon" viewBox="0 0 30 30" aria-hidden="true">
            <circle cx="15" cy="15" r="15" fill="var(--accent)"/>
            <path d="M10 8c1-1 2-1 3 0l1.5 2.5c.5 1 0 1.7-.8 2.3-.6.5-.4 1.2.3 2.2 1 1.2 1.7 1.8 2.6 2.1.7.2 1.200-.2 1.7-.8.6-.7 1.4-1 2.3-.4l2.2 1.6c.9.7.8 1.8-.3 2.8-1.5 1.4-4 1.3-7-1.2-3-2.6-5-5.6-5.2-8.1-.1-1.3.3-2.4 1-3z" fill="#fff"/>
          </svg>
          <span>02 6571 4826</span>
        </li>
        <li class="contact-item">
          <svg class="contact-icon" viewBox="0 0 30 30" aria-hidden="true">
            <circle cx="15" cy="15" r="15" fill="var(--accent)"/>
            <rect x="7.5" y="10" width="15" height="10.5" rx="1" fill="none" stroke="#fff" stroke-width="1.6"/>
            <path d="M7.8 10.5 15 16l7.2-5.5" fill="none" stroke="#fff" stroke-width="1.6"/>
          </svg>
          <span>info@harbourleafspinal.com.au</span>
        </li>
        <li class="contact-item">
          <svg class="contact-icon" viewBox="0 0 30 30" aria-hidden="true">
            <circle cx="15" cy="15" r="15" fill="var(--accent)"/>
            <g fill="none" stroke="#fff" stroke-width="1.4">
              <circle cx="15" cy="15" r="8"/>
              <ellipse cx="15" cy="15" rx="3.6" ry="8"/>
              <path d="M7 15h16M8.2 11h13.6M8.2 19h13.6"/>
            </g>
          </svg>
          <span>harbourleafspinal.com.au</span>
        </li>
      </ul>
    </div>
  </div>
</body>
</html>
```